Visitenkarten-Design für Sonnen-/Fensterschutz
Zielgruppe
KLR GmbH ist eine Firma, die Sonnenschutz und Fensterschutz anbieten.
'Ihr kompetenter Partner in Sachen Sonnenschutz- , Fenster- und Türtechnik. Sie erhalten echtes Handwerk aus dem Mühlviertel zu fairen Preisen.'
Unsere Zielgruppe sind Personen mit Haus, die am Land leben.
Firmenname: KLR GmbH
Slogan: Fenster & Sonnenschutz
Aufgabenstellung
Hier befindet sich das Logodesign: https://dl.qv/t-Rm8pQ2wZtB
Bitte ein schlichtes Design bereitstellen mit einer Dummy-Person:
Lutz Brenneke + Telefonnummer + Email
Die finalen Daten bitte erst am Schluss berücksichtigen (für Gewinnerdesign)
Gerne auch hintern + vorne bedruckbar bereitstellen.

```html
<!DOCTYPE html>
<html lang="de">
<head>
<meta charset="utf-8">
<title>KLR GmbH – Visitenkarte</title>
<link href="https://fonts.googleapis.com/css2?family=Poppins:ital,wght@0,400;0,600;1,400&display=swap" rel="stylesheet">
<style>
  :root {
    --canvas: #ffffff;
    --card-start: #e0691f;
    --card-end: #d3361e;
    --ink: #ffffff;
    --ink-soft: rgba(255,255,255,0.92);
  }
  * { margin: 0; padding: 0; box-sizing: border-box; }
  html, body {
    width: 1000px; height: 1200px; overflow: hidden;
    background: var(--canvas);
    font-family: "Poppins", sans-serif;
  }
  .sheet { position: relative; width: 1000px; height: 1200px; }
  .card {
    position: absolute; top: 170px;
    width: 402px; height: 259px;
    background: linear-gradient(90deg, var(--card-start) 0%, var(--card-end) 100%);
    box-shadow: 0 3px 8px rgba(0,0,0,0.18);
    color: var(--ink);
  }
  .card--front { left: 70px; }
  .card--back { left: 528px; }

  .brand {
    position: absolute; left: 0; right: 0; top: 92px;
    display: flex; flex-direction: column; align-items: center;
  }
  .brand__row { display: flex; align-items: center; gap: 14px; }
  .brand__mark { width: 26px; height: 26px; background: var(--ink); }
  .brand__name {
    font-weight: 600; font-size: 44px; line-height: 1; letter-spacing: 1px;
  }
  .brand__slogan {
    margin-top: 8px; font-size: 12.5px; letter-spacing: 0.4px; text-transform: uppercase;
  }

  .claim {
    position: absolute; left: 23px; top: 25px;
    font-style: italic; font-size: 15px; line-height: 20px; letter-spacing: 0.3px;
    color: var(--ink-soft);
  }
  .contact {
    position: absolute; left: 261px; top: 127px;
    font-size: 10.5px; line-height: 14px; letter-spacing: 0.3px; text-transform: uppercase;
  }
  .contact p + p { margin-top: 14px; }
</style>
</head>
<body>
<main class="sheet">
  <section class="card card--front" aria-label="Vorderseite">
    <div class="brand">
      <div class="brand__row">
        <span class="brand__mark" aria-hidden="true"></span>
        <span class="brand__name">KLR GmbH</span>
      </div>
      <span class="brand__slogan">Fenster &amp; Sonnenschutz</span>
    </div>
  </section>

  <section class="card card--back" aria-label="Rückseite">
    <p class="claim">»Ihr kompetenter<br>Partner in Sachen<br>Sonnenschutz-,<br>Fenster- und<br>Türtechnik. Sie<br>erhalten echtes<br>Handwerk aus dem<br>Mühlviertel zu fairen<br>Preisen.«</p>
    <div class="contact">
      <p>Lutz Brenneke<br>Lindenweg 7<br>4262 Ahornbach</p>
      <p>0720 31 58 46</p>
      <p>lutz@klr.at<br>www.klr.at</p>
    </div>
  </section>
</main>
</body>
</html>
```